Financial Sevices firm looking for Brochure design

Our company Veltmoor Capital and Holdings Limited (VeltHoldings)
i
Is an investment/advisory firm - www.veltholdings-grp.net
We invest in the energy sector in Africa and offer advisory services to Energy companies looking to invest in Africa. From oil and gas, to renewables (wind/solar). We are more focused on the "West African" Sub region
We need corporate brochure (Booklet style) to circulate to our corporate clients
We would like to see a design that considers the colours in our Logo (see website)
HI Guys, sorry been travelling. Seen some very good submissions and will be sending updates shortly
Reason: Dear Designers,
Thank you for participating in this project and for some of the great designs i've received so far. Unfortunately, due to the holidays, it has been difficult to consult with other members of my team. As a result, the project deadline is extended by about 12 days
I appreciate your understanding in the situation and looking forward to continuing the excellent collaboration in the coming days
Reason: Hi All,
Apologies for the multiple deadline extensions and thanks so much for all the designs which my team and I will be reviewing today and tomorrow.
We will be closing this project tomorrow by 6pm GMT (17th Jan 2014)
Thanks to all those that submitted such wonderful designs and goodluck!!
Project to be closed finally on 17th Jan 2014 at 6pm GMT
Banks, Investment Firms, Energy companies, Private Equity Funds
I have attached a Brochure that I created myself as an example of the type of information required but please also feel free to visit our website www.veltholdings-grp.net
Looking for any creative ideas you have to suplement the information provided.
Financial

```html
<!DOCTYPE html>
<html lang="en">
<head>
<meta charset="utf-8">
<title>VeltHoldings Company Profile – People, Profit and Planet</title>
<link href="https://fonts.googleapis.com/css2?family=Roboto:wght@300;400&display=swap" rel="stylesheet">
<style>
  :root {
    --backdrop: #e9e9ea;
    --paper: #ffffff;
    --ink: #4a4a4a;
    --ink-soft: #6d6d6d;
    --accent: #d6242a;
    --sky: #f1f1ef;
    --haze: #d9d7d0;
    --foliage: #8d8a6c;
    --earth: #a9875f;
    --dust: #c9a781;
  }
  * { box-sizing: border-box; margin: 0; padding: 0; }
  html, body {
    width: 1200px; height: 840px; overflow: hidden;
    background: var(--backdrop);
    font-family: "Roboto", Arial, sans-serif;
    color: var(--ink);
  }
  .spread {
    position: absolute; left: 50px; top: 40px;
    width: 1100px; height: 760px;
    display: flex;
    box-shadow: 0 6px 24px rgba(0,0,0,0.12);
  }
  .page { position: relative; width: 550px; height: 760px; overflow: hidden; }
  .page--mission { background: var(--paper); }

  .brand-name {
    position: absolute; top: 40px; right: 60px;
    display: flex; align-items: center; gap: 6px;
    font-size: 20px; font-weight: 400; color: var(--accent);
  }
  .brand-name .mark { width: 12px; height: 12px; background: var(--accent); }

  .section-label {
    position: absolute; top: 86px; left: 40px;
    font-size: 12px; font-weight: 300; color: var(--ink-soft);
  }
  .headline {
    position: absolute; top: 320px; left: 40px;
    font-size: 42px; font-weight: 300; line-height: 1.1; color: var(--ink);
  }
  .body-copy {
    position: absolute; top: 430px;
    width: 230px;
    font-size: 9.5px; font-weight: 300; line-height: 1.35; color: var(--ink);
  }
  .body-copy p { margin-bottom: 10px; }
  .body-copy--left { left: 40px; }
  .body-copy--right { left: 285px; }

  .competency { display: flex; gap: 12px; margin-bottom: 4px; }
  .competency__number {
    flex: 0 0 28px;
    font-size: 44px; font-weight: 300; line-height: 1; color: var(--accent);
  }
  .competency__text { padding-top: 2px; }

  .folio {
    position: absolute; bottom: 22px; left: 40px;
    font-size: 9px; font-weight: 300; color: var(--ink-soft);
  }

  .page--philosophy { background: var(--sky); }
  .photo-area {
    position: absolute; inset: 0;
    background: linear-gradient(180deg,
      var(--sky) 0%, var(--sky) 22%,
      var(--haze) 34%, var(--foliage) 50%,
      var(--earth) 68%, var(--dust) 100%);
  }
  .philosophy-statement {
    position: absolute; top: 30px; right: 40px;
    width: 275px;
    font-size: 14px; font-weight: 300; line-height: 1.35; color: var(--ink-soft);
  }
</style>
</head>
<body>
  <main class="spread">
    <section class="page page--mission">
      <div class="brand-name"><span class="mark"></span>VeltHoldings</div>
      <p class="section-label">Our Mission</p>
      <h1 class="headline">People,<br>Profit and Planet</h1>

      <div class="body-copy body-copy--left">
        <p>VeltHoldings is an indigenous investment and advisory firm with global networks and international expertise in infrastructure project finance</p>
        <p>VeltHoldings seeks to add value to its clients through its core competencies:</p>
        <div class="competency">
          <span class="competency__number">1</span>
          <p class="competency__text">Unique ability to deliver tailor-made solutions including structuring project and operating capital, project budget analysis, modeling, securing attractively-priced capital.</p>
        </div>
        <div class="competency">
          <span class="competency__number">2</span>
          <p class="competency__text">Collective experience in originating, appraising, structuring and financing investments in infrastructure assets worth over US $ 10 billion across Africa.</p>
        </div>
      </div>

      <div class="body-copy body-copy--right">
        <p>We are dedicated to promote the sustainable implementation of infrastructure and energy related projects in Africa through direct investments and by facilitating private and institutional investments. Our narrow sector focus enables us to provide in-depth services and insightful investment solutions.</p>
        <p>Our mission is to contribute to the implementation of robust infrastructure towards enhanced socio-economic development in Africa. To create the greatest value for our clients and investors through the efficient implementation of infrastructure and energy related projects across Africa.</p>
        <p>Our team brings a wealth of international expertise in the areas of transaction structuring, public-private partnerships (PPP), financial and economic modeling, legal and regulatory reform, and operations.</p>
      </div>

      <p class="folio">2 | Company Profile</p>
    </section>

    <section class="page page--philosophy">
      <div class="photo-area" role="img" aria-label="Photograph of two children at a village hand water pump with plastic containers, dry trees and a dusty ground under a pale sky"></div>
      <p class="philosophy-statement">Our investment philosophy integrates sustainability into a rigorous traditional investment process in order to deliver superior long-term results.</p>
    </section>
  </main>
</body>
</html>
```